Wine label design for my wife. Wine called "The Mirabel"

I need a wine label face lift of one of my premium wines in my collection. My wine sells in Harbor Lark's all over the States. My current label is called The Mirabel (my wife's name) and the illustration of her eyes is done by a well know artist from South Africa. I do not have to use this illustration and therefor I attached several pictures of her and her eyes, even when she was a little girl. The wine's also made in South Africa. This is a premium wine that we only sell 2000 bottles per year. The wine sells at 60 usd per bottle, The current label is too white. I also think her eyes should look more at the person buying it, than away from them.

Target Market(s)

Top end wine buyers

Font styles to use
Decorative
Script

Requirements
Must have
• 'The Mirabel' must be on the label
An illustration must be on the label
Basically all the info that's on the current label must be on by law. As per Sample
Nice to have
• Maybe some ideas of her whole face?
Should not have
• any gold colour

```html
<!DOCTYPE html>
<html lang="en">
<head>
<meta charset="utf-8">
<title>The Mirabel – Sauvignon Blanc 2017</title>
<link href="https://fonts.googleapis.com/css2?family=Cinzel:wght@400&family=IM+Fell+English+SC&display=swap" rel="stylesheet">
<style>
  :root {
    --backdrop-top: #f8e7cb;
    --backdrop-bottom: #bd9f7b;
    --label-taupe: #ab978b;
    --label-taupe-dark: #8f7e73;
    --label-white: #ffffff;
    --title-red: #c0141f;
    --varietal-grey: #9d9d9d;
    --producer-white: #ffffff;
    --ornament-tone: #e7ddd6;
    --portrait-light: #ececec;
    --portrait-mid: #c9c9c9;
  }
  * { margin: 0; padding: 0; box-sizing: border-box; }
  html, body {
    width: 1200px;
    height: 992px;
    overflow: hidden;
  }
  body {
    background: linear-gradient(180deg, var(--backdrop-top) 0%, var(--backdrop-top) 55%, var(--backdrop-bottom) 100%);
    position: relative;
  }
  .wine-label {
    position: absolute;
    left: 310px;
    top: 46px;
    width: 580px;
    height: 900px;
  }
  .label-shape {
    position: absolute;
    inset: 0;
    width: 580px;
    height: 900px;
    filter: drop-shadow(2px 3px 4px rgba(80, 60, 40, 0.35));
  }
  .label-content {
    position: absolute;
    left: 0;
    top: 41px;
    width: 580px;
    height: 794px;
  }
  .wine-name {
    position: absolute;
    left: 0;
    right: 0;
    top: 138px;
    text-align: center;
    font-family: "IM Fell English SC", serif;
    font-size: 92px;
    line-height: 1;
    letter-spacing: 3px;
    color: var(--title-red);
    white-space: nowrap;
  }
  .portrait-band {
    position: absolute;
    left: 18px;
    right: -3px;
    top: 322px;
    height: 206px;
    background: radial-gradient(ellipse at 50% 55%, var(--portrait-light) 0%, var(--portrait-light) 45%, var(--portrait-mid) 100%);
  }
  .varietal {
    position: absolute;
    left: 0;
    right: 0;
    top: 568px;
    text-align: center;
    font-family: "Cinzel", serif;
    font-size: 38px;
    line-height: 1;
    color: var(--varietal-grey);
    white-space: nowrap;
  }
  .producer {
    position: absolute;
    left: 0;
    right: 0;
    top: 706px;
    text-align: center;
    font-family: "Cinzel", serif;
    font-size: 36px;
    line-height: 1;
    color: var(--producer-white);
    white-space: nowrap;
  }
</style>
</head>
<body>
  <main class="wine-label">
    <svg class="label-shape" viewBox="0 0 580 900" width="580" height="900" aria-hidden="true">
      <defs>
        <linearGradient id="label-body-fill" x1="0" y1="0" x2="0" y2="1">
          <stop offset="0" stop-color="var(--label-taupe)"/>
          <stop offset="0.36" stop-color="var(--label-white)"/>
          <stop offset="0.68" stop-color="var(--label-white)"/>
          <stop offset="1" stop-color="var(--label-taupe-dark)"/>
        </linearGradient>
      </defs>
      <path class="crest-top" d="M94,43 C110,20 150,6 200,3 L380,3 C430,6 470,20 490,43 Z" fill="var(--label-taupe)"/>
      <rect class="label-body" x="0" y="41" width="580" height="794" fill="url(#label-body-fill)"/>
      <path class="crest-bottom" d="M94,833 C112,872 170,896 240,899 L340,899 C410,896 470,872 490,833 Z" fill="var(--label-taupe-dark)"/>
      <polygon class="rule-top-left" points="2,41 200,38.5 200,43.5" fill="var(--label-white)"/>
      <polygon class="rule-top-right" points="578,41 380,38.5 380,43.5" fill="var(--label-white)"/>
      <polygon class="rule-bottom-left" points="2,835 200,832.5 200,837.5" fill="var(--label-white)"/>
      <polygon class="rule-bottom-right" points="578,835 380,832.5 380,837.5" fill="var(--label-white)"/>
    </svg>
    <svg class="ornament-top" role="img" aria-label="Decorative white scrollwork flourish" viewBox="0 0 300 34" width="300" height="34" style="position:absolute;left:140px;top:8px;">
      <rect x="0" y="0" width="300" height="34" rx="17" fill="var(--ornament-tone)" opacity="0.55"/>
    </svg>
    <svg class="ornament-bottom" role="img" aria-label="Decorative white scrollwork flourish" viewBox="0 0 300 56" width="300" height="56" style="position:absolute;left:140px;top:838px;">
      <rect x="0" y="0" width="300" height="56" rx="28" fill="var(--ornament-tone)" opacity="0.45"/>
    </svg>
    <div class="label-content">
      <h1 class="wine-name">The Mirabel</h1>
      <div class="portrait-band" role="img" aria-label="Black and white illustration of Mirabel's eyes"></div>
      <p class="varietal">Sauvignon Blanc 2017</p>
      <p class="producer">Daniel Crest Wines</p>
    </div>
  </main>
</body>
</html>
```